Events and Parties web-site needs a Web Design

VoTrel needs a web design.
VoTrel means The Bees in Italian.
VoTrel target market is people who is organizing parties and events.
Our mission is that the parties and events of our clients exceed their expectations by providing them web and mobile tools.
Our vision is to be the best and biggest party web portal of the country.
The main features of our web site is to let people invite guests and search suppliers/providers. Guests will also confirm presence (RSVP) and buy presents/gifts at the site as well.
Our slogan is "Curta sua festa desde já !" that means "Enjoy our party now !" in Brazilian Portuguese.
The idea here is that the party starts now and not only at the scheduled date and time.
Updates
It seems that must have and nice to have briefing is not appearing to you as I filled. So I will type it agai here:
Our slogan text that is "Curta sua festa desde já !" that means "Enjoy your party now !".
Space to paid ads.
Language switch to Spanish. Brazilian Portuguese is our default language.
Logon form with 2 inputs: Email and password.
RSVP form with 2 inputs: Event ID and password
Kendro trusted site seal (SSL/HTTPS) logo.
Update to my briefing: Only event organizer and guests will be able to see details of the events/parties like photos/blog, guest list and etc. Suppliers will be searched and rated like stayvoro.com/roamgliq.
Target Market(s)
VoTrel target market is amateur and professional people who are organizing parties and events.
Our mission is that the parties and events of our clients exceed their expectations by providing them easy and fast web and mobile tools.
Our vision is to be the best and biggest party portal of our country.
The main features of our web site is to let people invite guests and search suppliers/providers. Guests will also confirm presence (RSVP) and buy presents at the site.
Industry/Entity Type
Events
Requirements
Must have
- Design and colors compliant with attached logo.
- Our slogan text that is "Curta sua festa desde já !" that means "Enjoy your party now !".
- Space to paid ads.
- Language switch to Spanish. Brazilian Portuguese is our default language.
- Logon form with 2 inputs: Email and password.
- RSVP form with 2 inputs: Event ID and password
- Kendro trusted site seal (SSL/HTTPS) logo.
Nice to have
- VoTrel stands for The Bees in Italian. It would be very nice to have a not so explicit idea that each user is a bee and VoTrel is the hive where party/event occurs.
Should not have
- No PageMill please.
- No infant/child oriented designs please. Our market is not only children birthdays but also other parties and events like marriages, corporate events and so on

```html
<!DOCTYPE html>
<html lang="pt-BR">
<head>
<meta charset="utf-8">
<title>VoTrel — Curta sua festa desde já !</title>
<link href="https://fonts.googleapis.com/css2?family=Merriweather:wght@400;700&family=Open+Sans:ital,wght@0,400;0,600;0,700;1,400;1,600&display=swap" rel="stylesheet">
<style>
:root{
  --honey:#f8b200;
  --honey-1:#e3a20f;
  --honey-2:#d4930a;
  --honey-3:#e9a912;
  --honey-4:#f6b500;
  --amber-text:#f5a600;
  --cocoa:#2d0a07;
  --plum-text:#5b3a3a;
  --footer:#b07d00;
  --line:#e6e6e6;
  --hero-bg:#f1f1f1;
  --soft:#f1f1f1;
  --grey-text:#8d8d8d;
  --body-text:#3b3b3b;
  --white:#ffffff;
}
*{box-sizing:border-box;margin:0;padding:0}
html,body{width:855px;height:1200px;overflow:hidden;background:var(--white)}
body{position:relative;font-family:"Open Sans",Arial,sans-serif;color:var(--body-text);font-size:8px}
.abs{position:absolute}

/* top bar */
.topbar{left:160px;top:0;width:535px;height:17px;background:var(--honey);color:var(--white);font-size:7px;font-weight:700}
.topbar .links{left:16px;top:3px;word-spacing:5px}
.topbar .contact{right:16px;top:3px}
.topbar .contact span{margin-left:12px}
.topbar svg{vertical-align:-1px;margin-right:3px}

/* header */
.header{left:160px;top:17px;width:535px;height:84px;background:var(--white);box-shadow:0 1px 2px rgba(0,0,0,.12)}
.brand{left:6px;top:16px;display:flex;align-items:center;gap:5px}
.brand-dot{width:14px;height:14px;border-radius:50%;background:var(--honey)}
.brand-name{font-family:"Open Sans",Arial,sans-serif;font-weight:600;font-size:17px;color:var(--cocoa)}
.brand-rule{left:0;top:55px;width:54px;height:2px;background:var(--honey)}
.social{left:427px;top:19px;display:flex;gap:3px}
.social i{display:block;width:16px;height:16px;border-radius:50%;background:#9a9a9a}
.nav{left:0;top:56px;width:535px;height:28px;border-top:1px solid var(--line);display:flex;font-size:8px;font-weight:600;color:#333}
.nav a{display:flex;align-items:center;justify-content:center;height:27px;border-right:1px solid var(--line);color:inherit;text-decoration:none}
.nav .search{margin-left:auto;width:41px;border-left:1px solid var(--line);border-right:0}

/* hero */
.hero{left:0;top:100px;width:855px;height:285px;background:var(--hero-bg)}
.slide-side{top:58px;width:138px;height:156px;box-shadow:0 2px 6px rgba(0,0,0,.2)}
.slide-left{left:107px;background:radial-gradient(circle at 40% 40%,#d9a51c,#6b4408 70%,#2a1803)}
.slide-right{left:643px;background:linear-gradient(160deg,#cfc6b6,#b79a86 50%,#8a7a66)}
.slide-main{left:245px;top:39px;width:398px;height:218px;background:linear-gradient(100deg,#7b7e84 0%,#9ea4ab 35%,#c9c4bb 60%,#5e5d61 85%,#d8d6d2 100%);box-shadow:0 3px 8px rgba(0,0,0,.25)}
.slide-main .taxi{position:absolute;left:0;bottom:0;width:210px;height:60px;background:linear-gradient(90deg,#8f6e1b,#e2b43a,#b48721)}
.slogan{font-family:"Merriweather",Georgia,serif;color:var(--white);font-size:15.5px;padding:0 7px;white-space:nowrap;height:31px;line-height:31px}
.slogan-pt{left:163px;top:222px;background:rgba(232,165,18,.82);padding-left:14px}
.slogan-en{left:163px;top:256px;height:29px;line-height:29px;background:rgba(45,10,7,.72)}
.arrow-tab{top:106px;width:31px;height:64px;background:var(--white);display:flex;align-items:center;justify-content:center}
.arrow-left{left:0;border-right:2px solid var(--cocoa)}
.arrow-right{left:824px;border-left:2px solid var(--cocoa)}

/* feature tiles */
.tiles{left:160px;top:377px;width:535px;height:101px;display:flex}
.tile{width:107px;height:101px;display:flex;flex-direction:column;align-items:center;padding-top:22px;color:var(--white);font-family:"Merriweather",Georgia,serif;font-weight:700;font-size:10px}
.tile .disc{width:40px;height:40px;border-radius:50%;background:var(--white);display:flex;align-items:center;justify-content:center;margin-bottom:8px}
.t1{background:var(--honey-1)}.t2{background:var(--honey-2)}.t3{background:var(--honey-3)}.t4{background:var(--honey-4)}.t5{background:var(--cocoa)}

/* content */
.content{left:160px;top:478px;width:535px;height:500px;border-left:1px solid var(--line);border-right:1px solid var(--line)}
.col-rule{top:478px;width:1px;height:500px;background:var(--line)}
.hr{height:1px;background:var(--line)}
.label{height:18px;line-height:18px;padding-left:6px;font-family:"Merriweather",Georgia,serif;font-weight:700;font-size:8px}
.label-honey{background:var(--honey);color:var(--cocoa)}
.label-cocoa{background:var(--cocoa);color:var(--white)}
.pager{position:absolute;right:4px;top:3px;display:flex;gap:2px}
.pager i{display:flex;width:11px;height:11px;border-radius:50%;background:var(--white);align-items:center;justify-content:center}
.para{font-size:8px;line-height:12.5px;color:var(--body-text)}
.field{height:18px;border:1px solid #dedede;font-size:6px;color:#aaa;padding-left:5px;line-height:16px}
.btn{height:18px;border:1px solid #dedede;font-size:6.5px;font-weight:700;color:#333;text-align:center;line-height:16px;background:#fafafa}
.seal{left:167px;top:953px;width:30px;height:23px;border:1px solid #b9b9b9;background:linear-gradient(#f4f4f4,#dcdcdc);border-radius:2px}

.news-thumb{width:36px;height:36px;border-radius:50%;background:var(--soft)}
.news-title{font-size:8px;font-weight:600;color:var(--plum-text);white-space:nowrap}
.news-date{font-size:6.5px;color:var(--grey-text)}
.video{left:324px;top:771px;width:207px;height:130px;background:var(--soft)}
.ad{left:580px;width:83px;height:26px;background:var(--soft)}

.date-badge{left:565px;width:27px}
.date-badge .m{height:11px;background:#7a5c5c;color:var(--white);font-size:6.5px;font-weight:700;text-align:center;line-height:11px}
.date-badge .d{height:22px;border:1px solid #ddd;border-top:0;font-size:12px;text-align:center;line-height:21px;color:#333}
.evt-title{left:601px;width:80px;font-size:8px;line-height:11px;font-weight:600;color:var(--amber-text)}
.evt-time{left:601px;font-size:6.5px;color:var(--grey-text)}

/* footer */
.footer{left:0;top:978px;width:855px;height:222px;background:var(--footer);color:var(--white)}
.f-head{top:37px;font-family:"Merriweather",Georgia,serif;font-weight:700;font-size:8px;color:var(--white)}
.f-bar{top:51px;width:22px;height:2px;background:var(--cocoa)}
.f-text{font-size:7.8px;line-height:12.4px;color:var(--white)}
.tag{height:17px;line-height:17px;background:var(--cocoa);color:var(--white);font-size:7.5px;padding-left:6px}
.tweet{font-size:7.5px;line-height:12.5px;font-style:italic;font-weight:600;width:112px}
.tweet b{font-weight:400}
.ago{font-size:6.5px;color:#f4e2b4}
.thumb{width:34px;height:34px;background:var(--soft)}
.bottombar{left:177px;top:194px;width:502px;height:28px;background:var(--honey);color:var(--cocoa);font-size:7px}
</style>
</head>
<body>

<!-- top utility bar -->
<div class="abs topbar">
  <div class="abs links">Link Link Link Link Link</div>
  <div class="abs contact">
    <span><svg width="7" height="7" viewBox="0 0 10 10"><path d="M2 0.5l2 2-1.2 1.4a6 6 0 003.3 3.3L7.5 6l2 2-1.3 1.6C4 9.5.5 6 .4 1.8z" fill="#fff"/></svg>1800-555-0192</span>
    <span><svg width="8" height="6" viewBox="0 0 10 7"><rect width="10" height="7" fill="#fff"/><path d="M0 0l5 4 5-4" stroke="#f8b200" fill="none"/></svg>hello@votrel-site.com</span>
  </div>
</div>

<!-- header -->
<header class="abs header">
  <div class="abs brand"><span class="brand-dot"></span><span class="brand-name">VoTrel</span></div>
  <div class="abs brand-rule"></div>
  <div class="abs social" aria-label="Redes sociais"><i></i><i></i><i></i><i></i><i></i></div>
  <nav class="abs nav">
    <a style="width:54px">Home</a>
    <a style="width:66px">About Us</a>
    <a style="width:68px">Courses&nbsp;<svg width="6" height="4" viewBox="0 0 6 4"><path d="M.5.5l2.5 2.5L5.5.5" stroke="#333" fill="none"/></svg></a>
    <a style="width:57px">Events</a>
    <a style="width:55px">News</a>
    <a style="width:56px">Gallery</a>
    <a style="width:74px;border-right:0">Contact Us</a>
    <a class="search"><svg width="9" height="9" viewBox="0 0 10 10"><circle cx="4" cy="4" r="3" stroke="#aaa" fill="none" stroke-width="1.2"/><path d="M6.3 6.3L9.3 9.3" stroke="#aaa" stroke-width="1.3"/></svg></a>
  </nav>
</header>

<!-- hero slider -->
<section class="abs hero">
  <div class="abs slide-side slide-left" role="img" aria-label="Close-up of sparkling golden champagne bubbles"></div>
  <div class="abs slide-side slide-right" role="img" aria-label="Crowd at an outdoor party with colourful balloons"></div>
  <div class="abs slide-main" role="img" aria-label="Businessman in a suit checking his watch on a city street with a yellow taxi"><div class="taxi"></div></div>
  <div class="abs arrow-tab arrow-left"><svg width="9" height="16" viewBox="0 0 9 16"><path d="M8 1L1 8l7 7" stroke="#f0a800" stroke-width="1.4" fill="none"/></svg></div>
  <div class="abs arrow-tab arrow-right"><svg width="9" height="16" viewBox="0 0 9 16"><path d="M1 1l7 7-7 7" stroke="#f0a800" stroke-width="1.4" fill="none"/></svg></div>
</section>
<div class="abs slogan slogan-pt">Curta sua festa desde já !</div>
<div class="abs slogan slogan-en">Enjoy our party now !</div>

<!-- feature tiles -->
<div class="abs tiles">
  <div class="tile t1"><span class="disc"><svg width="22" height="20" viewBox="0 0 22 20"><path d="M11 19S1 12.5 1 6.3A5 5 0 0111 4a5 5 0 0110 2.3C21 12.5 11 19 11 19z" fill="#e3a20f"/></svg></span>Link</div>
  <div class="tile t2"><span class="disc"><svg width="20" height="20" viewBox="0 0 20 20"><path d="M3 17l1-5L14 2l4 4L8 16z" fill="#d4930a"/></svg></span>Link</div>
  <div class="tile t3"><span class="disc"><svg width="22" height="21" viewBox="0 0 22 21"><path d="M11 1l3 6.5 7 .8-5.2 4.8 1.5 7L11 16.6 4.7 20l1.5-7L1 8.3l7-.8z" fill="#e9a912"/></svg></span>Link</div>
  <div class="tile t4"><span class="disc"><svg width="22" height="20" viewBox="0 0 22 20"><path d="M11 1L1 10h3v9h5v-6h4v6h5v-9h3z" fill="#f6b500"/></svg></span>Link</div>
  <div class="tile t5"><span class="disc"><svg width="20" height="14" viewBox="0 0 20 14"><rect width="20" height="14" rx="3" fill="#f8b200"/><path d="M8 4l5 3-5 3z" fill="#fff"/></svg></span>Take a Tour</div>
</div>

<!-- content area -->
<div class="abs content"></div>
<div class="abs col-rule" style="left:308px"></div>
<div class="abs col-rule" style="left:548px"></div>

<!-- left column -->
<div class="abs label label-honey" style="left:177px;top:491px;width:114px">R.S.V.P.»</div>
<p class="abs para" style="left:177px;top:520px;width:120px">Li Europan lingues es membres del sam familie.</p>
<div class="abs field" style="left:177px;top:553px;width:114px">Event ID<span style="position:absolute;right:0;top:-1px;width:18px;height:18px;border-left:1px solid #dedede"><svg width="18" height="16" viewBox="0 0 18 16"><path d="M7 6l2-2 2 2M7 10l2 2 2-2" stroke="#555" fill="none"/></svg></span></div>
<div class="abs field" style="left:177px;top:578px;width:114px">Password</div>
<div class="abs btn" style="left:254px;top:603px;width:37px">Search</div>
<div class="abs hr" style="left:160px;top:636px;width:148px"></div>

<div class="abs label label-honey" style="left:177px;top:646px;width:114px">Log In.»</div>
<p class="abs para" style="left:177px;top:675px;width:120px">Li Europan lingues es membres del sam familie.</p>
<div class="abs field" style="left:177px;top:708px;width:114px">Email</div>
<div class="abs field" style="left:177px;top:733px;width:114px">Password</div>
<div class="abs btn" style="left:254px;top:758px;width:37px">Go</div>
<div class="abs hr" style="left:160px;top:784px;width:148px"></div>

<div class="abs label label-cocoa" style="left:177px;top:798px;width:114px">Newsletter »</div>
<p class="abs para" style="left:177px;top:827px;width:120px">Li Europan lingues es membres del sam familie.</p>
<div class="abs field" style="left:177px;top:860px;width:114px">Email Address</div>
<div class="abs btn" style="left:243px;top:885px;width:48px">Subscribe</div>
<div class="abs seal" role="img" aria-label="Secure connection seal"></div>

<!-- middle column -->
<div class="abs label label-honey" style="left:324px;top:491px;width:207px">News »
  <span class="pager"><i><svg width="5" height="6" viewBox="0 0 5 6"><path d="M4 .5L1 3l3 2.5" stroke="#2d0a07" fill="none" stroke-width="1.2"/></svg></i><i><svg width="5" height="6" viewBox="0 0 5 6"><path d="M1 .5L4 3 1 5.5" stroke="#2d0a07" fill="none" stroke-width="1.2"/></svg></i></span>
</div>

<div class="abs news-thumb" style="left:324px;top:523px"></div>
<div class="abs news-title" style="left:371px;top:521px">To an English person, it will seem like simply</div>
<div class="abs news-date" style="left:371px;top:533px">Feb 13h, 2014</div>
<p class="abs para" style="left:371px;top:547px;width:165px">A un Angleso it va semblar un simplificat Angles</p>

<div class="abs news-thumb" style="left:324px;top:592px"></div>
<div class="abs news-title" style="left:371px;top:590px">To an English person, it will seem like simply</div>
<div class="abs news-date" style="left:371px;top:602px">Feb 13h, 2014</div>
<p class="abs para" style="left:371px;top:616px;width:165px">A un Angleso it va semblar un simplificat Angles</p>

<div class="abs news-thumb" style="left:324px;top:661px"></div>
<div class="abs news-title" style="left:371px;top:659px">To an English person, it will seem like simply</div>
<div class="abs news-date" style="left:371px;top:671px">Feb 13h, 2014</div>
<p class="abs para" style="left:371px;top:685px;width:165px">A un Angleso it va semblar un simplificat Angles</p>
<div class="abs hr" style="left:308px;top:722px;width:240px"></div>

<div class="abs label label-cocoa" style="left:324px;top:740px;width:207px">Video Tour »
  <span class="pager"><i><svg width="5" height="6" viewBox="0 0 5 6"><path d="M4 .5L1 3l3 2.5" stroke="#2d0a07" fill="none" stroke-width="1.2"/></svg></i><i><svg width="5" height="6" viewBox="0 0 5 6"><path d="M1 .5L4 3 1 5.5" stroke="#2d0a07" fill="none" stroke-width="1.2"/></svg></i></span>
</div>
<div class="abs video" role="img" aria-label="Video tour player"></div>
<p class="abs para" style="left:324px;top:909px;width:200px">It wasn't a dream. His room, a proper human room although a little too small</p>

<!-- right column -->
<div class="abs label label-honey" style="left:565px;top:493px;width:114px">Sponsors »
  <span class="pager"><i><svg width="5" height="6" viewBox="0 0 5 6"><path d="M4 .5L1 3l3 2.5" stroke="#2d0a07" fill="none" stroke-width="1.2"/></svg></i><i><svg width="5" height="6" viewBox="0 0 5 6"><path d="M1 .5L4 3 1 5.5" stroke="#2d0a07" fill="none" stroke-width="1.2"/></svg></i></span>
</div>
<div class="abs ad" style="top:524px" role="img" aria-label="Paid advertising slot"></div>
<div class="abs ad" style="top:560px" role="img" aria-label="Paid advertising slot"></div>
<div class="abs ad" style="top:597px" role="img" aria-label="Paid advertising slot"></div>
<div class="abs hr" style="left:548px;top:651px;width:147px"></div>

<div class="abs label label-honey" style="left:565px;top:675px;width:114px;height:19px;line-height:19px">Save the Date »</div>

<div class="abs date-badge" style="top:707px"><div class="m">FEB</div><div class="d">08</div></div>
<div class="abs evt-title" style="top:706px">The new common will be more&nbsp; simple</div>
<div class="abs evt-time" style="top:730px">9:00am to 1:00pm</div>

<div class="abs date-badge" style="top:752px"><div class="m">FEB</div><div class="d">10</div></div>
<div class="abs evt-title" style="top:751px">The new common will be more&nbsp; simple</div>
<div class="abs evt-time" style="top:775px">9:00am to 1:00pm</div>

<div class="abs date-badge" style="top:796px"><div class="m">FEB</div><div class="d">14</div></div>
<div class="abs evt-title" style="top:795px">The new common will be more&nbsp; simple</div>
<div class="abs evt-time" style="top:819px">9:00am to 1:00pm</div>

<!-- footer -->
<footer class="abs footer">
  <div class="abs f-head" style="left:177px">About Us</div>
  <div class="abs f-bar" style="left:177px"></div>
  <p class="abs f-text" style="left:177px;top:67px;width:122px">Quisque bibendum erat feugiat rhoncus tincidunt ipsum mi facilisis nisl, nec eleifend enim massa ac purus. Integer malesuada faucibus auctor vivamus accumsan justo.</p>

  <div class="abs f-head" style="left:306px">Tag Cloud</div>
  <div class="abs f-bar" style="left:306px"></div>
  <div class="abs tag" style="left:306px;top:70px;width:43px">Education</div>
  <div class="abs tag" style="left:356px;top:70px;width:46px;padding-left:13px">Funny</div>
  <div class="abs tag" style="left:306px;top:93px;width:36px">College</div>
  <div class="abs tag" style="left:349px;top:93px;width:39px">Parties</div>
  <div class="abs tag" style="left:306px;top:116px;width:22px">Art</div>
  <div class="abs tag" style="left:333px;top:116px;width:34px">Design</div>
  <div class="abs tag" style="left:373px;top:116px;width:32px">Music</div>
  <div class="abs tag" style="left:306px;top:139px;width:55px;padding-left:15px">March</div>

  <div class="abs f-head" style="left:436px">Social Feed</div>
  <div class="abs f-bar" style="left:436px"></div>
  <p class="abs tweet" style="left:436px;top:67px"><b>@Nerilo</b> imperdiet adipiscing elit ac fermentum. nullam et</p>
  <div class="abs ago" style="left:436px;top:95px">about 6 hours ago</div>
  <p class="abs tweet" style="left:436px;top:118px"><b>@VoTrel</b> imperdiet adipiscing elit ac fermentum. nullam et</p>
  <div class="abs ago" style="left:436px;top:146px">about 6 hours ago</div>

  <div class="abs f-head" style="left:570px">Photo Gallery »</div>
  <div class="abs f-bar" style="left:570px"></div>
  <div class="abs thumb" style="left:564px;top:65px" role="img" aria-label="Party photo"></div>
  <div class="abs thumb" style="left:604px;top:65px" role="img" aria-label="Party photo"></div>
  <div class="abs thumb" style="left:644px;top:65px" role="img" aria-label="Party photo"></div>
  <div class="abs thumb" style="left:564px;top:105px" role="img" aria-label="Party photo"></div>
  <div class="abs thumb" style="left:604px;top:105px" role="img" aria-label="Party photo"></div>
  <div class="abs thumb" style="left:644px;top:105px" role="img" aria-label="Party photo"></div>

  <div class="abs bottombar">
    <span class="abs" style="left:10px;top:10px">© Copyright&nbsp; VoTrel</span>
    <span class="abs" style="right:10px;top:10px">Top <svg width="6" height="4" viewBox="0 0 6 4"><path d="M.5 3.5L3 1l2.5 2.5" stroke="#2d0a07" fill="none"/></svg></span>
  </div>
</footer>

</body>
</html>
```